property investment and development company needs a website

we need a website that looks professional and portrays trust for people looking to us to buy their house or investors looking to invest or joint venture with us.
We are based in the west midlands in the UK.
we deal mainly with residential housing, house to flats conversions, HMO's (houses in multiple ocupancy).
we require the website as a first point of contact with potential sellers, renters and investors so links or contact details that are easy to access or see would be good.
I have had logos designed by a plan hollow member and these can be used as guidance for the colour and style of the site.
Target Market(s)
joint venture investment partners, people looking to sell their house, people looking to rent from us.
Coding
Coded - Design and coding required
Number of Pages Required
3 page
Requirements
Must have
- project a professional appearance
- visable contact details

```html
<!DOCTYPE html>
<html lang="en">
<head>
<meta charset="utf-8">
<title>Halden Homes</title>
<link rel="stylesheet" href="https://fonts.googleapis.com/css2?family=Cinzel:wght@400;700&family=Lato:wght@400;700;900&family=Quicksand:wght@400;500&display=swap">
<style>
:root{
  --gold:#c9a86b;
  --gold-dark:#b8965a;
  --ink:#1f1f1f;
  --text:#555;
  --light:#efefef;
  --white:#fff;
  --footer-top:#333;
  --footer-bottom:#111;
}
*{margin:0;padding:0;box-sizing:border-box}
html,body{width:1200px;height:2448px;overflow:hidden;background:var(--white)}
body{position:relative;font-family:"Quicksand",sans-serif;color:var(--text)}
.abs{position:absolute}

/* header */
.brand{left:77px;top:22px;display:flex;align-items:center;gap:12px}
.brand-mark{width:44px;height:44px;background:var(--gold)}
.brand-name{font-family:"Cinzel",serif;font-weight:400;font-size:27px;line-height:30px;color:var(--ink);letter-spacing:1px}
.call{right:77px;top:22px;display:flex;align-items:center;gap:10px}
.call-label{font-family:"Quicksand",sans-serif;font-size:15px;color:var(--gold);letter-spacing:.5px}
.call-number{font-family:"Cinzel",serif;font-size:29px;color:var(--ink);line-height:32px}

/* nav */
.nav{left:0;top:99px;width:1200px;height:62px;background:var(--gold)}
.nav-list{position:absolute;left:77px;top:0;display:flex;list-style:none;height:62px}
.nav-list li{font-family:"Lato",sans-serif;font-size:16px;color:var(--white);height:62px;display:flex;align-items:center;justify-content:center;position:relative}
.nav-list li.active{background:linear-gradient(#2a2a2a,#000);width:125px}
.nav-list li.sep::after{content:"";position:absolute;right:0;top:16px;height:32px;width:1px;background:rgba(255,255,255,.35)}
.search{left:791px;top:108px;width:333px;height:46px;border:1px solid rgba(255,255,255,.6);display:flex}
.search span{flex:1;font-family:"Lato",sans-serif;font-size:13px;color:var(--white);padding:14px 18px}
.search-btn{width:46px;height:44px;background:var(--ink);display:flex;align-items:center;justify-content:center}

/* hero */
.hero{left:0;top:161px;width:1200px;height:521px;background:linear-gradient(180deg,#3d4654 0%,#5b5a55 45%,#6b5a3e 70%,#2e2b26 100%)}
.hero-title{left:0;top:330px;width:1200px;text-align:center;font-family:"Lato",sans-serif;font-weight:900;font-size:84px;color:var(--white);letter-spacing:-1px}
.hero-sub{left:290px;top:432px;width:620px;height:73px;background:rgba(40,40,40,.5);text-align:center;font-family:"Quicksand",sans-serif;font-weight:500;font-size:18px;line-height:27px;color:var(--white);padding-top:9px}

/* service cards */
.card{top:724px;width:511px;height:281px;background:linear-gradient(135deg,#3a3a3a,#1c1c1c)}
.card.sell{background:linear-gradient(135deg,#3b4356,#232a39)}
.card-frame{position:absolute;left:20px;top:21px;right:20px;bottom:21px;border:1px solid var(--gold)}
.card-title{position:absolute;left:0;top:93px;width:100%;text-align:center;font-family:"Cinzel",serif;font-weight:700;font-size:31px;color:var(--white);letter-spacing:1px}
.card-text{position:absolute;left:60px;right:60px;top:142px;text-align:center;font-size:13.5px;line-height:23px;color:var(--white)}
.card-arrow{position:absolute;left:50%;bottom:10px;transform:translateX(-50%)}

/* welcome */
.welcome{left:0;top:1068px;width:1200px;height:520px;background:var(--light)}
.welcome-photo{left:77px;top:1139px;width:474px;height:375px;background:linear-gradient(135deg,#e9e6e0,#c9c3b8 55%,#8d8b87)}
.welcome-kicker{left:608px;top:1137px;font-family:"Cinzel",serif;font-size:24px;color:var(--ink);letter-spacing:1px}
.welcome-title{left:608px;top:1164px;font-family:"Cinzel",serif;font-weight:700;font-size:46px;color:var(--ink);letter-spacing:1px}
.welcome-copy{left:614px;top:1245px;width:490px;font-size:13.5px;line-height:27px}
.welcome-copy p+p{margin-top:13px}
.btn{background:var(--gold);color:var(--white);font-family:"Cinzel",serif;font-weight:700;font-size:20px;display:flex;align-items:center;justify-content:center;letter-spacing:1px}
.learn{left:615px;top:1455px;width:187px;height:57px}

/* contact */
.contact-title{left:0;top:1642px;width:1200px;text-align:center;font-family:"Cinzel",serif;font-weight:700;font-size:48px;color:var(--ink);letter-spacing:1px}
.contact-sub{left:0;top:1702px;width:1200px;text-align:center;font-size:15.5px;color:var(--text)}
.field{border:1px solid #ddd;font-size:13px;color:#999;padding:14px 16px;background:var(--white)}
.field.focus{border-color:var(--gold);color:var(--gold)}
.f-name{left:246px;top:1758px;width:333px;height:46px}
.f-phone{left:246px;top:1813px;width:333px;height:46px}
.f-email{left:246px;top:1866px;width:333px;height:46px}
.f-message{left:590px;top:1758px;width:364px;height:154px;padding:14px 19px}
.checks{left:0;top:1932px;width:1200px;display:flex;justify-content:center;gap:44px;font-family:"Lato",sans-serif;font-size:13.5px;color:var(--ink)}
.check{display:flex;align-items:center;gap:24px}
.box{width:16px;height:16px;border:1px solid #bbb;background:#f4f4f4}
.submit{left:522px;top:1986px;width:156px;height:56px}

/* footer */
.footer{left:0;top:2104px;width:1200px;height:281px;background:linear-gradient(var(--footer-top),var(--footer-bottom))}
.f-head{top:2139px;font-family:"Cinzel",serif;font-weight:700;font-size:18px;color:var(--white);letter-spacing:1px}
.f-about{left:79px;top:2182px;width:240px;font-size:13.5px;line-height:25px;color:#bbb}
.read-more{left:79px;top:2317px;font-size:13.5px;font-style:italic;color:var(--gold);text-decoration:underline}
.sitemap{left:346px;top:2182px;list-style:none}
.sitemap li{font-size:13.5px;color:#ccc;line-height:35.5px;padding-left:19px;position:relative}
.sitemap li::before{content:"";position:absolute;left:0;top:15px;width:5px;height:5px;border-radius:50%;background:var(--gold)}
.contact-list{left:610px;top:2182px;list-style:none}
.contact-list li{display:flex;gap:18px;font-size:13.5px;line-height:25px;color:#ccc}
.contact-list svg{flex:none;width:20px;margin-top:3px}
.f-brand{left:908px;top:2204px;display:flex;align-items:center;gap:12px}
.f-brand .brand-name{color:var(--gold)}
.social{left:934px;top:2275px;display:flex;gap:7px}
.social span{width:41px;height:41px;border:1px solid var(--gold);border-radius:50%}
.copyright{left:0;top:2385px;width:1200px;height:63px;background:var(--gold);text-align:center;font-size:13.5px;color:var(--white);line-height:63px}
.copyright b{font-weight:500}
</style>
</head>
<body>

<header>
  <div class="abs brand">
    <span class="brand-mark"></span>
    <div class="brand-name">HALDEN<br>HOMES</div>
  </div>
  <div class="abs call">
    <svg width="46" height="46" viewBox="0 0 24 24" aria-hidden="true"><path fill="#c9a86b" d="M6.6 10.8a15.1 15.1 0 0 0 6.6 6.6l2.2-2.2c.3-.3.7-.4 1-.2 1.1.4 2.3.6 3.6.6.6 0 1 .4 1 1V20c0 .6-.4 1-1 1A17 17 0 0 1 3 4c0-.6.4-1 1-1h3.5c.6 0 1 .4 1 1 0 1.3.2 2.5.6 3.6.1.3 0 .7-.2 1z"/></svg>
    <div>
      <div class="call-label">Call Us Today :</div>
      <div class="call-number">01632 960418</div>
    </div>
  </div>
</header>

<nav class="abs nav">
  <ul class="nav-list">
    <li class="active">HOME</li>
    <li class="sep" style="width:140px">INVEST</li>
    <li class="sep" style="width:114px">SELL</li>
    <li class="sep" style="width:135px">ABOUT US</li>
    <li style="width:164px">CONTACT US</li>
  </ul>
</nav>
<div class="abs search">
  <span>Search....</span>
  <div class="search-btn"><svg width="16" height="16" viewBox="0 0 16 16" aria-hidden="true"><circle cx="6.5" cy="6.5" r="4.5" fill="none" stroke="#fff" stroke-width="2"/><path d="M10 10l4 4" stroke="#fff" stroke-width="2.2"/></svg></div>
</div>

<section>
  <div class="abs hero" role="img" aria-label="Modern glass-fronted building lit at dusk"></div>
  <h1 class="abs hero-title">HALDEN HOMES</h1>
  <p class="abs hero-sub">We ensure that whatever your property needs are we deliver<br>bespoke services for our clients</p>
</section>

<section>
  <div class="abs card" style="left:77px" role="img" aria-label="Cupped hands around a patch of grass">
    <div class="card-frame"></div>
    <h2 class="card-title">INVEST</h2>
    <p class="card-text">We have our own portfolio and we are active investors, so our finger is on the pulse.</p>
    <svg class="card-arrow" width="46" height="16" viewBox="0 0 46 16" aria-hidden="true"><path d="M0 8h36" stroke="#c9a86b" stroke-width="4"/><path d="M32 1l12 7-12 7z" fill="#c9a86b"/></svg>
  </div>
  <div class="abs card sell" style="left:612px" role="img" aria-label="Hand holding house keys in front of a home">
    <div class="card-frame"></div>
    <h2 class="card-title">SELL</h2>
    <p class="card-text">We undertake the necessary market research to evaluate an option that works.</p>
    <svg class="card-arrow" width="46" height="16" viewBox="0 0 46 16" aria-hidden="true"><path d="M0 8h36" stroke="#c9a86b" stroke-width="4"/><path d="M32 1l12 7-12 7z" fill="#c9a86b"/></svg>
  </div>
</section>

<section>
  <div class="abs welcome">
    <svg class="abs" style="left:0;top:0" width="1200" height="520" aria-hidden="true"><polygon points="0,145 0,520 474,520" fill="#c9a86b"/></svg>
  </div>
  <div class="abs welcome-photo" role="img" aria-label="Clients shaking hands with an agent over house plans"></div>
  <div class="abs welcome-kicker">WELCOME TO</div>
  <h2 class="abs welcome-title">HALDEN HOMES</h2>
  <div class="abs welcome-copy">
    <p>We are a property development and investment company that have our own portfolio and we are active investors who pride ourselves in expanding our business organically.</p>
    <p>We ensure that whatever your property needs are we deliver bespoke services for our clients. For investors, sellers, landlords and tenants we bring knowledge to your next property decision, allowing you to make an informed decision.</p>
  </div>
  <div class="abs btn learn">LEARN MORE</div>
</section>

<section>
  <h2 class="abs contact-title">CONTACT US</h2>
  <p class="abs contact-sub">If you have any question for contact us Today !</p>
  <div class="abs field focus f-name">Name *</div>
  <div class="abs field f-phone">Phone *</div>
  <div class="abs field f-email">Email *</div>
  <div class="abs field f-message">Message *</div>
  <div class="abs checks">
    <div class="check">SELLERS <span class="box"></span></div>
    <div class="check">RENTERS <span class="box"></span></div>
    <div class="check">INVESTORS <span class="box"></span></div>
  </div>
  <div class="abs btn submit">SUBMIT</div>
</section>

<footer>
  <div class="abs footer"></div>
  <h3 class="abs f-head" style="left:79px">ABOUT US</h3>
  <p class="abs f-about">We are a property development and investment company that have our own portfolio and we are active investors who pride ourselves in expanding our business...</p>
  <span class="abs read-more">Read More...»</span>

  <h3 class="abs f-head" style="left:346px">SITEMAP</h3>
  <ul class="abs sitemap">
    <li>Home</li><li>Invest</li><li>Sell</li><li>About</li><li>Contact</li>
  </ul>

  <h3 class="abs f-head" style="left:614px">CONTACT US</h3>
  <ul class="abs contact-list">
    <li style="height:67px"><svg height="28" viewBox="0 0 20 28" aria-hidden="true"><path fill="#c9a86b" d="M10 0a9 9 0 0 0-9 9c0 7 9 19 9 19s9-12 9-19a9 9 0 0 0-9-9zm0 13a4 4 0 1 1 0-8 4 4 0 0 1 0 8z"/></svg><span>12 Fenwick Lane, Ashbury,<br>Westshire, AB12 3CD</span></li>
    <li style="height:37px"><svg height="20" viewBox="0 0 24 24" aria-hidden="true"><path fill="#c9a86b" d="M6.6 10.8a15.1 15.1 0 0 0 6.6 6.6l2.2-2.2c.3-.3.7-.4 1-.2 1.1.4 2.3.6 3.6.6.6 0 1 .4 1 1V20c0 .6-.4 1-1 1A17 17 0 0 1 3 4c0-.6.4-1 1-1h3.5c.6 0 1 .4 1 1 0 1.3.2 2.5.6 3.6.1.3 0 .7-.2 1z"/></svg><span>01632 960418</span></li>
    <li style="height:38px"><svg height="22" viewBox="0 0 20 24" aria-hidden="true"><rect x="4" y="1" width="12" height="22" rx="2" fill="none" stroke="#c9a86b" stroke-width="2.5"/><circle cx="10" cy="19" r="1.5" fill="#c9a86b"/></svg><span>07700 900233</span></li>
    <li><svg height="16" viewBox="0 0 20 16" aria-hidden="true"><rect width="20" height="16" fill="#c9a86b"/><path d="M0 1l10 8 10-8" fill="none" stroke="#333" stroke-width="1.5"/></svg><span>info@haldenhomes.co.uk</span></li>
  </ul>

  <div class="abs f-brand">
    <span class="brand-mark"></span>
    <div class="brand-name">HALDEN<br>HOMES</div>
  </div>
  <div class="abs social" aria-label="Social links">
    <span></span><span></span><span></span>
  </div>

  <div class="abs copyright">©<b>HALDEN HOMES</b> - 2019 All Rights Reserved.</div>
</footer>

</body>
</html>
```